Card Design to Advertise New Business

I am looking to have a card designed so that I can pass it out to help promote my business. I have never done this before so I honestly do not know where to start with any ideas. I am providing my website address to help. I provide math tutoring, test prep, and schooling options.

I am looking for a card bigger than a business card but smaller than a flyer. Something front and back that I can pass out.

Business Information
Phone: 470-526-1984
Website: www.brightmaplestudyhub.com
Address: 418 Larkwood Rd Ste 210 Marietta GA 30068
Email: brightmapleservices@kestrelpostmail.com

Services:
Math Tutoring
College Entrance Test Prep
Group and Private Sessions
Fully Accredited Private School

Target Market(s)

Middle and High School Students

Industry/Entity Type

Education

Requirements
Must have
• Information from my website

```html
<!DOCTYPE html>
<html lang="en">
<head>
<meta charset="utf-8">
<title>Bright Maple Study Hub – Promo Card</title>
<link href="https://fonts.googleapis.com/css2?family=Figtree:wght@300;400;500;600;700;800;900&family=Kalam:wght@700&display=swap" rel="stylesheet">
<style>
  :root{
    --royal:#3a67cc;
    --tomato:#cc2a00;
    --sky:#4aa6d6;
    --lime:#14c514;
    --mustard:#d4c300;
    --violet:#6b4bb8;
    --ink-violet:#5636a8;
    --board:#006837;
    --frame:#8a6540;
    --frame-dark:#6f4f30;
    --white:#ffffff;
    --paper:#ffffff;
    --bg:#e9e9e9;
  }
  *{margin:0;padding:0;box-sizing:border-box}
  html,body{width:969px;height:1200px;overflow:hidden;background:var(--bg)}
  body{font-family:"Figtree",Arial,sans-serif}
  .card{position:relative;width:969px;height:1200px;background:var(--paper);overflow:hidden}

  .hero-photo{position:absolute;left:0;top:0;width:969px;height:491px;
    background:linear-gradient(100deg,#c9bfb6 0%,#d97a68 18%,#e9c3a6 35%,#86aee0 48%,#7a5a48 60%,#e6c9a9 72%,#5f86d2 88%,#e8d3a0 100%);}

  .headline{position:absolute;left:50px;top:352px;width:872px;height:140px;background:var(--royal);
    border-radius:22px;color:var(--white);text-align:center;text-transform:uppercase}
  .headline .lead{display:block;font-size:41px;font-weight:300;line-height:1;padding-top:16px;letter-spacing:.2px}
  .headline .lead b{font-weight:800}
  .headline .main{display:block;font-size:67px;font-weight:900;line-height:1;margin-top:4px;letter-spacing:.5px}

  .tagline{position:absolute;left:50px;top:495px;width:872px;height:70px;background:var(--tomato);
    border-radius:35px;color:var(--white);font-size:36px;font-weight:600;line-height:70px;text-align:center}

  .stripe{position:absolute;left:0;width:969px}
  .stripe.sky{top:772px;height:36px;background:var(--sky)}
  .stripe.lime{top:808px;height:36px;background:var(--lime)}
  .stripe.tomato{top:844px;height:37px;background:var(--tomato)}
  .stripe.mustard{top:881px;height:35px;background:var(--mustard)}

  .offer{position:absolute;left:30px;top:622px;width:310px;height:240px}
  .offer svg{position:absolute;inset:0}
  .offer p{position:absolute;left:0;top:58px;width:310px;transform:rotate(-15deg);
    font-family:"Kalam",cursive;font-weight:700;color:var(--white);font-size:37px;line-height:1.15;text-align:center}

  .board{position:absolute;left:364px;top:608px;width:552px;height:311px;background:var(--frame);
    border-radius:8px;box-shadow:inset 0 -8px 0 var(--frame-dark)}
  .board-face{position:absolute;left:17px;top:15px;width:517px;height:282px;background:var(--board);border-radius:4px;
    padding:22px 0 0 32px;color:var(--white)}
  .board-face h2{font-size:46px;font-weight:800;line-height:1;margin-bottom:10px;text-shadow:1px 2px 2px rgba(0,0,0,.35)}
  .services{list-style:none}
  .services li{font-size:28.5px;font-weight:500;line-height:44.5px;text-shadow:1px 2px 2px rgba(0,0,0,.35);
    display:flex;align-items:center;white-space:nowrap}
  .services li::before{content:"";width:14px;height:14px;border-radius:50%;background:var(--white);margin-right:13px;flex:none}

  .footer{position:absolute;left:0;top:916px;width:969px;height:284px;background:var(--violet)}

  .brand{position:absolute;left:38px;top:966px;width:255px;height:234px;background:var(--white);text-align:center}
  .brand-dot{width:122px;height:122px;border-radius:50%;background:var(--royal);margin:17px auto 12px}
  .brand-name{font-size:25px;font-weight:800;color:var(--royal);line-height:1.05;text-transform:uppercase}

  .contact{position:absolute;left:319px;top:966px;width:609px;height:234px;background:var(--white);padding:15px 0 0 25px;font-style:normal}
  .contact-row{display:flex;align-items:center;height:50px;color:var(--ink-violet);font-weight:600;white-space:nowrap}
  .contact-row .icon{width:43px;height:43px;border-radius:50%;background:var(--ink-violet);flex:none;margin-right:12px;
    display:flex;align-items:center;justify-content:center}
  .contact-row .icon svg{width:26px;height:26px;fill:none;stroke:var(--white);stroke-width:1.8;stroke-linecap:round;stroke-linejoin:round}
  .contact-row.phone{height:50px;margin-bottom:4px}
  .contact-row.phone span{font-size:48px;font-weight:700;letter-spacing:.5px}
  .contact-row span{font-size:22px}
  .contact-row.email span{font-size:20px}
</style>
</head>
<body>
<main class="card">
  <div class="hero-photo" role="img" aria-label="Photo of smiling middle school students working at desks with a teacher helping them"></div>

  <h1 class="headline">
    <span class="lead">More than just <b>math tutoring</b></span>
    <span class="main">We are path coaches</span>
  </h1>
  <p class="tagline">Path Coaching and Math Tutoring for all ages</p>

  <div class="stripe sky"></div>
  <div class="stripe lime"></div>
  <div class="stripe tomato"></div>
  <div class="stripe mustard"></div>

  <div class="offer">
    <svg viewBox="0 0 310 240" aria-hidden="true">
      <path d="M8 96 C2 66 40 56 80 42 C130 24 175 -4 240 6 C300 16 312 50 296 90 C286 118 306 146 284 184 C260 222 196 220 146 226 C94 232 40 248 18 214 C4 190 20 160 10 132 C6 120 10 108 8 96 Z" fill="#3a67cc"/>
    </svg>
    <p>Lower Rates with<br>Memberships or<br>Packages</p>
  </div>

  <section class="board">
    <div class="board-face">
      <h2>Our Services:</h2>
      <ul class="services">
        <li>Math Tutoring</li>
        <li>Group and Private Sessions</li>
        <li>College Entrance Test Prep</li>
        <li>Fully Accredited Private School</li>
      </ul>
    </div>
  </section>

  <footer class="footer"></footer>

  <div class="brand">
    <div class="brand-dot"></div>
    <div class="brand-name">Bright Maple<br>Study Hub</div>
  </div>

  <address class="contact">
    <div class="contact-row phone">
      <span class="icon"><svg viewBox="0 0 24 24"><path d="M6 3h3l1.5 5-2 1.5a11 11 0 0 0 6 6l1.5-2 5 1.5v3a2 2 0 0 1-2 2A17 17 0 0 1 4 5a2 2 0 0 1 2-2z"/></svg></span>
      <span>470-526-1984</span>
    </div>
    <div class="contact-row email">
      <span class="icon"><svg viewBox="0 0 24 24"><rect x="3" y="6" width="18" height="12" rx="1"/><path d="M3 7l9 7 9-7M3 18l7-6M21 18l-7-6"/></svg></span>
      <span>brightmapleservices@kestrelpostmail.com</span>
    </div>
    <div class="contact-row web">
      <span class="icon"><svg viewBox="0 0 24 24"><circle cx="12" cy="12" r="9"/><path d="M3 12h18M12 3c3 3 3 15 0 18M12 3c-3 3-3 15 0 18M5 7h14M5 17h14"/></svg></span>
      <span>www.brightmaplestudyhub.com</span>
    </div>
    <div class="contact-row pin">
      <span class="icon"><svg viewBox="0 0 24 24"><path d="M12 21s-6-6.5-6-11a6 6 0 0 1 12 0c0 4.5-6 11-6 11z"/><circle cx="12" cy="10" r="2.3"/></svg></span>
      <span>418 Larkwood Rd Ste 210 Marietta GA 30068</span>
    </div>
  </address>
</main>
</body>
</html>
```